KTR Consulting

I need an A4 one page flyer I can provide to clients briefly explaining my skills and experience and fee. I am a legal consultant specialising in construction projects.

Industry/Entity Type

Legal

Requirements
Nice to have
• Clean, simple design - corporate but not boring
Should not have
• Too busy or complex design

```html
<!DOCTYPE html>
<html lang="en">
<head>
<meta charset="utf-8">
<title>KTR Consulting – Simon Lowe</title>
<link href="https://fonts.googleapis.com/css2?family=Open+Sans:wght@400;600;700&display=swap" rel="stylesheet">
<style>
:root{
  --page-bg:#ececec;
  --paper:#ffffff;
  --brand-blue:#1b5eab;
  --accent-cyan:#2aa7df;
  --text:#4a4a4a;
  --text-dark:#2b2b2b;
  --sky-light:#e6f0f9;
  --sky-mid:#c7dcef;
  --glass-dark:#3d6687;
  --glass-light:#9dbdd5;
}
*{margin:0;padding:0;box-sizing:border-box}
html,body{width:1200px;height:810px;overflow:hidden;background:var(--page-bg)}
body{font-family:"Open Sans",sans-serif;color:var(--text);position:relative}
.flyer{
  position:absolute;left:320px;top:9px;width:581px;height:822px;
  background:var(--paper);transform:scale(.963);transform-origin:0 0;overflow:hidden;
  box-shadow:0 2px 10px rgba(0,0,0,.12);
}
.sky{
  position:absolute;left:0;top:380px;width:581px;height:442px;
  background:linear-gradient(180deg,rgba(255,255,255,0) 0%,var(--sky-light) 30%,var(--sky-mid) 55%,var(--sky-light) 80%,#f4f8fb 100%);
}
.building-photo{
  position:absolute;left:230px;top:530px;width:351px;height:292px;
  background:linear-gradient(150deg,var(--glass-light) 0%,var(--glass-dark) 55%,#6f95b4 100%);
  -webkit-mask-image:linear-gradient(180deg,transparent 0%,#000 40%),linear-gradient(90deg,transparent 0%,#000 35%);
  -webkit-mask-composite:source-in;
  mask-image:linear-gradient(180deg,transparent 0%,#000 40%),linear-gradient(90deg,transparent 0%,#000 35%);
  mask-composite:intersect;
}
.brand{position:absolute;left:171px;top:36px;display:flex;align-items:center;gap:8px}
.brand-dot{width:50px;height:50px;border-radius:50%;background:var(--brand-blue)}
.brand-name{font-size:31px;font-weight:600;color:var(--brand-blue);text-transform:uppercase;letter-spacing:-.3px}
.portrait{position:absolute;left:40px;top:97px;width:95px;height:116px;background:linear-gradient(180deg,#d8d8d8,#9a9a9a 70%,#3a3a3a)}
.person-name{position:absolute;left:0;width:174px;top:218px;text-align:center;font-size:14px;font-weight:700;color:var(--text-dark)}
.contacts{position:absolute;left:17px;top:263px;list-style:none}
.contacts li{display:flex;align-items:center;gap:5px;height:18px;font-size:8.6px;color:var(--text);margin-bottom:22px}
.contacts li.email{font-size:7.4px;margin-bottom:24px}
.contacts svg{width:17px;height:17px;flex:none}
.banner{position:absolute;left:180px;top:112px;width:388px;height:21px}
.banner svg{position:absolute;inset:0}
.banner span{position:relative;display:block;padding:3px 0 0 11px;font-size:10px;font-weight:700;color:#fff}
.bio{position:absolute;left:184px;top:144px;width:380px;font-size:9.3px;line-height:13.7px}
.bio p{margin-bottom:13.7px}
.bio ul{list-style:none;margin:0 0 13.7px;padding-right:28px}
.bio li{position:relative;padding-left:8px;margin-bottom:2px}
.bio li::before{content:"";position:absolute;left:1px;top:6px;width:3px;height:3px;border-radius:50%;background:var(--accent-cyan)}
.bio .summary{font-weight:700;color:var(--text-dark)}
</style>
</head>
<body>
<main class="flyer">
  <div class="sky" role="img" aria-label="Soft blue sky backdrop"></div>
  <div class="building-photo" role="img" aria-label="Photograph of a modern glass office building seen from below"></div>

  <header class="brand">
    <span class="brand-dot"></span>
    <span class="brand-name">KTR Consulting</span>
  </header>

  <div class="portrait" role="img" aria-label="Black and white portrait photo of Simon Lowe"></div>
  <h1 class="person-name">Simon Lowe</h1>

  <ul class="contacts">
    <li>
      <svg viewBox="0 0 18 18"><circle cx="9" cy="9" r="8" fill="none" stroke="var(--brand-blue)" stroke-width="1.2"/><path d="M6.3 4.8c.5-.3 1-.2 1.2.3l.7 1.5c.2.4 0 .8-.3 1l-.6.4c.5 1.3 1.4 2.3 2.6 3l.5-.5c.3-.3.7-.4 1.1-.2l1.4.8c.4.2.5.8.2 1.2l-.5.6c-.6.6-1.6.7-2.4.3-2.3-1.2-4-3.2-4.7-5.7-.2-.9.1-1.9.8-2.4z" fill="var(--brand-blue)"/></svg>
      0400 218 530
    </li>
    <li class="email">
      <svg viewBox="0 0 18 18"><circle cx="9" cy="9" r="8" fill="none" stroke="var(--brand-blue)" stroke-width="1.2"/><rect x="4.5" y="6" width="9" height="6.2" rx=".6" fill="var(--brand-blue)"/><path d="M4.8 6.4 9 9.6l4.2-3.2" fill="none" stroke="#fff" stroke-width=".9"/></svg>
      simon.lowe@ktrconsulting.com.au
    </li>
    <li>
      <svg viewBox="0 0 18 18"><circle cx="9" cy="9" r="8" fill="none" stroke="var(--brand-blue)" stroke-width="1.2"/><g fill="none" stroke="var(--brand-blue)" stroke-width=".9"><circle cx="9" cy="9" r="4.8"/><ellipse cx="9" cy="9" rx="2.1" ry="4.8"/><path d="M4.2 9h9.6M5 6.6h8M5 11.4h8"/></g></svg>
      www.ktrconsulting.com.au
    </li>
  </ul>

  <div class="banner">
    <svg viewBox="0 0 388 21" preserveAspectRatio="none"><polygon points="0,0 388,0 368,21 0,21" fill="var(--brand-blue)"/></svg>
    <span>Procurement, Risk Management and Major Projects</span>
  </div>

  <section class="bio">
    <p>Simon is the Managing Director of KTR Consulting, a boutique legal and commercial advisory consulting firm specialising in procurement, risk management and major project delivery. He is currently a Consultant to Harlow Partners and a guest lecturer at Southern Coast University in procurement and construction law.</p>
    <p style="margin-bottom:1px">Simon's expertise is in the delivery of major projects and covers all phases of project delivery including:</p>
    <ul>
      <li>Project development (including risk identification and analysis)</li>
      <li>Choosing the most appropriate procurement strategies</li>
      <li>EOI and RFT preparation, submissions and evaluation</li>
      <li>Negotiating and drafting a broad range of contracts e.g. goods and/or services supply agreements, consultancy agreements, construction contracts (ECI, D&amp;C, Works, EPC, EPCM, Managing Contractor, Construction Management, O&amp;M, FM) and other ancillary services agreements</li>
      <li>Contract management</li>
      <li>Reviewing lessons learnt to improve procurement management moving forward</li>
    </ul>
    <p>Simon has previously worked as a projects lawyer with Ashby Crane Lawyers and Bellamy Stone Partners (in Melbourne), as well as in house as Acting General Counsel of Riverside Airport and as corporate counsel with Coastal Hydro. He has also held various legal roles in the public sector, including as a corporate lawyer with the State Department of Transport and as a legal advisor to the Attorney-General of the State.</p>
    <p class="summary">Simon has extensive experience in procurement and major project delivery in a broad range of industries including the transport, mining, commercial property development, education and energy sectors.</p>
  </section>
</main>
</body>
</html>
```